Coffee Package Design

We need a new package design for a coffee company. Need to be a mix between modern and classic design combined together. We are open to different ideas.
We changing our product name from Café Verlona to Café Rostelli. The picture upload
shows what the product looks like. We want something completely different. The name of the company should go on the back of the package.
Updates

Hello Everyone,

Please read description, we are going with a new name and design for the product.

Café Rostelli. Café Verlona is what we are replacing with Café Rostelli, we are looking for new

look and design, please submit new designs.

There is a change in the description. Please take out Premium coffee blend and replace with Italian Roast.                                    

Industry/Entity Type

Cafe

Requirements
Must have
• You can use up to 6 colors.
Please put these items on design: Café Rostelli (this is the product name), Regular Premium Blend Coffee, 100% Arabica,
Dumbrell & Sons (name of the company), Tyler, TX on the back of the package

The file uploaded is an example of one of our products and how the package film
is sized.

```html
<!DOCTYPE html>
<html lang="en">
<head>
<meta charset="UTF-8">
<title>Café Rostelli – Italian Roast Package</title>
<link href="https://fonts.googleapis.com/css2?family=Sacramento&family=Mulish:wght@400&display=swap" rel="stylesheet">
<style>
  :root {
    --paper: #ffffff;
    --roast-red: #8b0000;
    --honey: #fdb120;
    --latte: #bfa06c;
    --script: "Sacramento", cursive;
    --sans: "Mulish", sans-serif;
  }
  * { margin: 0; padding: 0; box-sizing: border-box; }
  html, body { width: 1200px; height: 726px; overflow: hidden; background: var(--paper); }
  .canvas { position: relative; width: 1200px; height: 726px; }

  .package-film {
    position: absolute; left: 18px; top: 64px; width: 1158px; height: 584px;
    border-radius: 22px; overflow: hidden; background: var(--roast-red);
  }
  .top-band { position: absolute; left: 0; top: 0; width: 100%; height: 34px; background: var(--honey); }
  .bottom-band { position: absolute; left: 0; bottom: 0; width: 100%; height: 26px; background: var(--latte); }
  .seam-bar { position: absolute; left: 552px; top: 0; width: 46px; height: 558px; background: var(--honey); }

  .front-pattern {
    position: absolute; left: 0; top: 128px; width: 552px; height: 288px;
    background: var(--latte);
    border-top: 3px solid var(--honey); border-bottom: 3px solid var(--honey);
  }

  .name-label {
    position: absolute; left: 186px; top: 210px; width: 366px; height: 124px;
    background: var(--honey); border-radius: 12px 0 0 12px;
  }
  .product-name {
    position: absolute; left: 14px; top: 6px;
    font-family: var(--script); font-size: 74px; line-height: 1;
    color: var(--roast-red); white-space: nowrap; font-weight: 400;
  }
  .product-variant {
    position: absolute; right: 8px; bottom: 12px;
    font-family: var(--sans); font-size: 16px; color: var(--roast-red);
  }

  .bean-origin {
    position: absolute; left: 30px; top: 536px;
    font-family: var(--sans); font-size: 12px; color: var(--latte);
  }
  .company-name {
    position: absolute; left: 598px; width: 560px; top: 518px; text-align: center;
    font-family: var(--script); font-size: 36px; color: var(--latte); letter-spacing: 2px;
  }
</style>
</head>
<body>
<div class="canvas">
  <div class="package-film">
    <div class="top-band"></div>
    <div class="seam-bar"></div>
    <div class="front-pattern" role="img" aria-label="Honeycomb pattern band in tan cells with golden outlines"></div>
    <div class="name-label">
      <h1 class="product-name">Café Rostelli</h1>
      <p class="product-variant">Italian Roast</p>
    </div>
    <p class="bean-origin">100% Arabica</p>
    <p class="company-name">Dumbrell &amp; Sons</p>
    <div class="bottom-band"></div>
  </div>
</div>
</body>
</html>
```